Start-up beard care company needs packaging label designed.

We are a new business called WhiskerNook that sells high quality and natural beard care products. We require a wrap-around label design for our first product which is beard oil. The beard oil is held in 1oz/30ml glass amber bottles. The label size in inches is: 3.83" x 3.07"
We need one design however we have 4 scents: Stonehaven, Duskmoss, Peach Harbor and Still Meadow. So we need 4 labels each with a different scent name but with the same overall design. We are looking for a simple and eye catching design. The design should look clean, sleek and professional. We do not want the label to be clustered with information and images everywhere.
Brief:
Rules to follow:
• Colour Scheme: The label should be white with black writing.
• Font: The font used should be Maven Pro
Information that needs to be included on every label:
On the front of the label:
Name of oil: Stonehaven/Peach Harbor/ Duskmoss/ Still Meadow, BEARD OIL, Our logo (Attached file 7), shop: www.whiskernook-shop.example,
On the Back of the label:
ALL NATURAL INGREDIENTS, MAY CONTAIN ALLERGENS, MADE IN UK, FOR EXTERNAL USE ONLY, 1 fl oz/30ml, Directions: place a few drops on your hand and massage gently into your beard.
Information specific to scent (Should be placed on the back of the label):
• Stonehaven - Ingredients: Base Oils: Jojoba, Argan, Castor, Grapeseed and Sweet Almond Oil. Essential Oils: Sandalwood and Cedarwood
• Peach Harbor - Ingredients: Base Oils: Jojoba, Argan, Castor, Grapeseed and Sweet Almond Oil.
Essential Oils: Tea Tree, Lemon, Lime and Sweet Orange
• Duskmoss - Ingredients: Base Oils: Jojoba, Argan, Castor, Grapeseed and Sweet Almond Oil. Essential Oils: Cedarwood, Cinnamon and Patchouli
• Still Meadow - Ingredients: Base Oils: Jojoba, Argan, Castor, Grapeseed and Sweet Almond Oil.
Examples of label designs that we like are attached. File 6 is one of our own designs for the front of the label. It demonstrates the simple and sleek look that we are aiming for. An Image of the amber bottle that will hold the beard oil is also attached. File 7 is an example of how we would like the information on the back to be presented.
Updates
We have updated our brief, please take a look!Thanks. Added Sunday, September 13, 2015
I have added my logo in vector format (.ai). It is file number 7.
Thanks.
Target Market(s)
Men with beards, ages 18+
Industry/Entity Type
Hair And Beauty
Font styles to use
Other font styles liked:
- Maven Pro
Look and feel

```html
<!DOCTYPE html>
<html lang="en">
<head>
<meta charset="utf-8">
<title>WhiskerNook Beard Oil – Label Options</title>
<link href="https://fonts.googleapis.com/css2?family=Maven+Pro:wght@400;500;700&family=Arimo:wght@400&display=swap" rel="stylesheet">
<style>
  :root {
    --ink: #1d1d1d;
    --ink-soft: #555555;
    --paper: #ffffff;
    --edge: #dcdcdc;
    --page: #ffffff;
  }
  * { box-sizing: border-box; margin: 0; padding: 0; }
  html, body {
    width: 1200px;
    height: 2828px;
    overflow: hidden;
    background: var(--page);
    color: var(--ink);
    font-family: "Maven Pro", sans-serif;
  }
  .sheet { position: relative; width: 1200px; height: 2828px; }

  .sheet-note {
    position: absolute;
    left: 46px;
    top: 36px;
    font-family: "Arimo", sans-serif;
    font-size: 19px;
    line-height: 1.35;
    color: var(--ink);
  }

  .label {
    position: absolute;
    width: 370px;
    height: 450px;
    background: var(--paper);
    border: 1px solid var(--edge);
    border-radius: 6px;
    padding: 40px 34px 30px;
    display: flex;
    flex-direction: column;
    align-items: center;
    text-align: center;
  }
  .label--one   { left: 95px;  top: 440px; }
  .label--two   { left: 700px; top: 440px; }
  .label--three { left: 95px;  top: 1370px; }
  .label--four  { left: 700px; top: 1370px; }
  .label--five  { left: 400px; top: 2160px; }

  .caption {
    position: absolute;
    font-family: "Arimo", sans-serif;
    font-size: 19px;
    color: var(--ink-soft);
  }
  .caption--one   { left: 95px;  top: 955px; }
  .caption--two   { left: 700px; top: 955px; }
  .caption--three { left: 95px;  top: 1885px; }
  .caption--four  { left: 700px; top: 1885px; }
  .caption--five  { left: 730px; top: 2665px; }

  /* brand mark stand-in */
  .brand { display: flex; flex-direction: column; align-items: center; }
  .brand-row { display: flex; align-items: center; gap: 10px; }
  .brand-square { width: 24px; height: 24px; background: var(--ink); }
  .brand-name { font-size: 30px; font-weight: 700; color: var(--ink); letter-spacing: -0.3px; }
  .brand-tagline { font-size: 9px; color: var(--ink-soft); letter-spacing: 0.5px; margin-top: 2px; }

  .rule { width: 100%; height: 2px; background: var(--ink); }
  .rule--thin { height: 1px; }
  .rule--thick { height: 4px; }

  .scent { font-weight: 400; font-size: 44px; letter-spacing: 1px; line-height: 1; }
  .scent--bold { font-weight: 700; }

  .product { font-size: 20px; letter-spacing: 1px; }
  .volume { font-size: 14px; color: var(--ink); }
  .shop { font-size: 13px; }
  .url { font-size: 17px; font-weight: 500; }

  .flanked { display: flex; align-items: center; gap: 12px; justify-content: center; width: 100%; }
  .flanked::before, .flanked::after { content: ""; height: 1.5px; background: var(--ink); flex: 0 0 40px; }
  .flanked--wide::before, .flanked--wide::after { flex: 1 1 auto; }

  /* option one */
  .spec-row { display: flex; width: 100%; border: 1.5px solid var(--ink); }
  .spec-row span { flex: 1; padding: 8px 4px; font-size: 17px; }
  .spec-row span + span { border-left: 1.5px solid var(--ink); font-size: 14px; }
  .url-box { width: 100%; border-top: 2px solid var(--ink); border-bottom: 2px solid var(--ink); padding: 6px 0; }

  /* option three */
  .hatch-row { display: flex; width: 100%; align-items: center; gap: 10px; }
  .hatch-row .product { font-size: 20px; letter-spacing: 0; }
  .hatch { flex: 1; height: 14px; }
</style>
</head>
<body>
<main class="sheet">
  <p class="sheet-note">Suggestion for packaging ; white glass bottle with black plug 30ml<br>All 5 examples of design that I submitted.</p>

  <!-- option 1 -->
  <section class="label label--one">
    <div class="brand">
      <div class="brand-row"><span class="brand-square"></span><span class="brand-name">WhiskerNook</span></div>
      <span class="brand-tagline">Care for modern gentlemen</span>
    </div>
    <div class="rule" style="margin-top:22px"></div>
    <h2 class="scent" style="margin:30px 0 28px">DUSKMOSS</h2>
    <div class="spec-row"><span>BEARD OIL</span><span>1 fl oz/30ml</span></div>
    <p class="shop" style="margin-top:34px;font-weight:700">/SHOP/</p>
    <p class="url url-box" style="margin-top:6px">www.whiskernook-shop.example</p>
  </section>
  <p class="caption caption--one">whiskernook_1</p>

  <!-- option 2 -->
  <section class="label label--two">
    <div class="brand">
      <div class="brand-row"><span class="brand-square"></span><span class="brand-name">WhiskerNook</span></div>
      <span class="brand-tagline">Care for modern gentlemen</span>
    </div>
    <div class="rule rule--thin" style="margin-top:24px"></div>
    <h2 class="scent" style="margin:24px 0 22px">DUSKMOSS</h2>
    <div class="rule rule--thin"></div>
    <p class="product flanked" style="margin-top:10px">BEARD OIL</p>
    <p class="volume" style="margin-top:4px">1 fl oz/30ml</p>
    <p class="shop flanked" style="margin-top:50px">Shop</p>
    <p class="url" style="margin-top:4px">www.whiskernook-shop.example</p>
  </section>
  <p class="caption caption--two">whiskernook_2</p>

  <!-- option 3 -->
  <section class="label label--three">
    <div class="brand">
      <div class="brand-row"><span class="brand-square"></span><span class="brand-name">WhiskerNook</span></div>
      <span class="brand-tagline">Care for modern gentlemen</span>
    </div>
    <h2 class="scent" style="margin-top:40px;align-self:flex-start">Duskmoss</h2>
    <div class="rule rule--thick" style="margin-top:10px"></div>
    <div class="hatch-row" style="margin-top:14px">
      <span class="product">Beard Oil</span>
      <svg class="hatch" viewBox="0 0 120 14" preserveAspectRatio="none" aria-hidden="true">
        <g stroke="#1d1d1d" stroke-width="1.6">
          <line x1="2" y1="14" x2="8" y2="0"/><line x1="10" y1="14" x2="16" y2="0"/><line x1="18" y1="14" x2="24" y2="0"/>
          <line x1="26" y1="14" x2="32" y2="0"/><line x1="34" y1="14" x2="40" y2="0"/><line x1="42" y1="14" x2="48" y2="0"/>
          <line x1="50" y1="14" x2="56" y2="0"/><line x1="58" y1="14" x2="64" y2="0"/><line x1="66" y1="14" x2="72" y2="0"/>
          <line x1="74" y1="14" x2="80" y2="0"/><line x1="82" y1="14" x2="88" y2="0"/><line x1="90" y1="14" x2="96" y2="0"/>
          <line x1="98" y1="14" x2="104" y2="0"/><line x1="106" y1="14" x2="112" y2="0"/><line x1="114" y1="14" x2="120" y2="0"/>
        </g>
      </svg>
    </div>
    <p class="shop" style="margin-top:52px">Shop</p>
    <p class="url" style="margin-top:4px">www.whiskernook-shop.example</p>
    <p class="volume" style="margin-top:4px">1 fl oz/30ml</p>
  </section>
  <p class="caption caption--three">whiskernook_3</p>

  <!-- option 4 -->
  <section class="label label--four">
    <div class="brand">
      <div class="brand-row"><span class="brand-square"></span><span class="brand-name">WhiskerNook</span></div>
      <span class="brand-tagline">Care for modern gentlemen</span>
    </div>
    <h2 class="scent flanked flanked--wide" style="margin-top:42px;font-size:42px;letter-spacing:0">duskmoss</h2>
    <p class="product" style="margin-top:10px;letter-spacing:0">beard oil</p>
    <div class="rule rule--thin" style="margin-top:14px"></div>
    <p class="shop flanked flanked--wide" style="margin-top:40px">shop</p>
    <p class="url" style="margin-top:4px">www.whiskernook-shop.example</p>
    <p class="volume" style="margin-top:4px">1 fl oz/30ml</p>
  </section>
  <p class="caption caption--four">whiskernook_4</p>

  <!-- option 5 -->
  <section class="label label--five">
    <div class="brand">
      <div class="brand-row"><span class="brand-square"></span><span class="brand-name">WhiskerNook</span></div>
      <span class="brand-tagline">Care for modern gentlemen</span>
    </div>
    <div class="rule rule--thin" style="margin-top:24px"></div>
    <h2 class="scent scent--bold" style="margin:22px 0 20px">DUSKMOSS</h2>
    <div class="rule"></div>
    <p class="product" style="margin-top:10px;font-weight:500">BEARD OIL</p>
    <p class="volume" style="margin-top:4px">1 fl oz/30ml</p>
    <p class="shop flanked" style="margin-top:46px">Shop</p>
    <p class="url" style="margin-top:4px">www.whiskernook-shop.example</p>
  </section>
  <p class="caption caption--five">whiskernook_5</p>
</main>
</body>
</html>
```